Electrical Contracting Business card design

I would like a business card design for a new electrical business. I would like the print R.MOLT ELECTRICAL in large block lettering (spot gloss) on the front with atoms flying in a circle around the letter "A" of R.MOLT. Dark blue background, red lettering with the southern cross stars splashed in between the background and lettering.

On the rear of the card I would like the centre to have a box with 2 or 3 lines in it ( a space to write a time and date for the job to take place) surrounded by a big mass of confusing looking cables or a circuit diagram (something that would overwhelm people trying to make sense of it).

Thank you, I hope this isn't to detailed

Industry/Entity Type

Electrical

Contact Information for Business Card

R.MOLT ELECTRICAL
Phone: Brenn 0417853302
Brennr@mailvista.example
EC:47063

```html
<!DOCTYPE html>
<html lang="en">
<head>
<meta charset="utf-8">
<title>R.MOLT Electrical – Business Card</title>
<link href="https://fonts.googleapis.com/css2?family=Lato:wght@400;700;900&display=swap" rel="stylesheet">
<style>
  :root {
    --page-bg: #d9dbe0;
    --navy: #0f1446;
    --navy-deep: #0a0e36;
    --red: #e8503c;
    --cyan: #3bb8e8;
    --circuit-light: #3fb2e6;
    --circuit-mid: #1c6fc0;
    --circuit-dark: #0c1d5c;
    --panel: #f4f5f8;
    --ink: #1d2a5c;
    --rule: #8c93ad;
  }
  * { box-sizing: border-box; margin: 0; padding: 0; }
  html, body { width: 1200px; height: 926px; overflow: hidden; }
  body {
    background: var(--page-bg);
    font-family: "Lato", sans-serif;
    position: relative;
  }
  .card {
    position: absolute;
    left: 240px;
    width: 720px;
    height: 411px;
    overflow: hidden;
    box-shadow: 0 6px 18px rgba(0,0,0,0.18);
  }
  .card--front { top: 38px; background: var(--navy); }
  .card--back  { top: 477px; }

  /* Front */
  .star-decoration {
    position: absolute;
    left: 60px; top: -10px;
    width: 520px; height: 440px;
    background: radial-gradient(circle at 50% 50%, rgba(60,70,140,0.35) 0%, rgba(40,50,120,0.18) 45%, rgba(15,20,70,0) 72%);
  }
  .brand-mark {
    position: absolute;
    left: 62px; top: 148px;
    display: flex; align-items: center; gap: 10px;
  }
  .brand-mark__dot {
    width: 22px; height: 22px; border-radius: 50%;
    background: var(--red);
  }
  .brand-mark__name {
    color: var(--red);
    font-weight: 900;
    font-size: 26px;
    letter-spacing: 1px;
  }
  .business-name {
    position: absolute;
    left: 300px; top: 130px;
    color: var(--red);
    font-weight: 900;
    font-size: 38px;
    letter-spacing: 1px;
  }
  .contact-list {
    position: absolute;
    left: 300px; top: 196px;
    list-style: none;
    font-size: 20px;
    line-height: 30px;
    letter-spacing: 0.5px;
  }
  .contact-list__label {
    display: inline-block;
    width: 46px;
    color: var(--cyan);
  }
  .contact-list__value { color: var(--red); }

  /* Back */
  .circuit-field {
    position: absolute; inset: 0;
    background:
      radial-gradient(ellipse at 10% 50%, var(--circuit-light) 0%, rgba(63,178,230,0) 55%),
      linear-gradient(120deg, var(--circuit-mid) 0%, var(--circuit-dark) 70%, #081444 100%);
  }
  .appointment {
    position: absolute;
    left: 110px; top: 36px;
    width: 530px; height: 300px;
    background: var(--panel);
    padding: 18px 26px 0 24px;
    color: var(--ink);
  }
  .appointment__title {
    text-align: center;
    font-weight: 700;
    font-size: 22px;
    margin-bottom: 14px;
  }
  .appointment__row {
    display: flex; align-items: flex-end;
    height: 44px;
    border-bottom: 1px solid var(--rule);
    font-size: 15px;
    padding-bottom: 4px;
  }
  .appointment__date { width: 190px; }
  .appointment__time { flex: 1; }
  .appointment__choice {
    display: flex; align-items: center; gap: 5px;
    margin-left: 16px;
    font-size: 14px;
  }
  .appointment__box {
    width: 12px; height: 12px;
    border: 1.5px solid var(--ink);
  }
</style>
</head>
<body>

<section class="card card--front" aria-label="Card front">
  <div class="star-decoration" role="img" aria-label="Faint Southern Cross star outline behind the lettering"></div>
  <div class="brand-mark">
    <span class="brand-mark__dot"></span>
    <span class="brand-mark__name">R.MOLT</span>
  </div>
  <h1 class="business-name">R.MOLT ELECTRICAL</h1>
  <ul class="contact-list">
    <li><span class="contact-list__label">P:</span><span class="contact-list__value">0417853302 (Brenn)</span></li>
    <li><span class="contact-list__label">M:</span><span class="contact-list__value">Brennr@mailvista.example</span></li>
    <li><span class="contact-list__label">EC:</span><span class="contact-list__value">47063</span></li>
  </ul>
</section>

<section class="card card--back" aria-label="Card back">
  <div class="circuit-field" role="img" aria-label="Dense blue circuit board and hexagon pattern"></div>
  <div class="appointment">
    <h2 class="appointment__title">Appointment</h2>
    <div class="appointment__row"><span class="appointment__date">Date:</span><span class="appointment__time">Time:</span><span class="appointment__choice"><span class="appointment__box"></span>am</span><span class="appointment__choice"><span class="appointment__box"></span>pm</span></div>
    <div class="appointment__row"><span class="appointment__date">Date:</span><span class="appointment__time">Time:</span><span class="appointment__choice"><span class="appointment__box"></span>am</span><span class="appointment__choice"><span class="appointment__box"></span>pm</span></div>
    <div class="appointment__row"><span class="appointment__date">Date:</span><span class="appointment__time">Time:</span><span class="appointment__choice"><span class="appointment__box"></span>am</span><span class="appointment__choice"><span class="appointment__box"></span>pm</span></div>
    <div class="appointment__row"><span class="appointment__date">Date:</span><span class="appointment__time">Time:</span><span class="appointment__choice"><span class="appointment__box"></span>am</span><span class="appointment__choice"><span class="appointment__box"></span>pm</span></div>
    <div class="appointment__row"><span class="appointment__date">Date:</span><span class="appointment__time">Time:</span><span class="appointment__choice"><span class="appointment__box"></span>am</span><span class="appointment__choice"><span class="appointment__box"></span>pm</span></div>
  </div>
</section>

</body>
</html>
```